Capital Management company needs a web design

We have a domain name and logo but need hosting and design. Please look at the Must-Haves section.

Target Market(s)

banking industry and investors

Industry/Entity Type

Investment

Coding

Coded - Design and coding required

Number of Pages Required

1 page

Font styles to use
Sans Serif

Requirements
Must have
• Picture(s) of skyscraper skyline (can be of Manhattan, Chicago, or any other major city in the USA).
• Please use the three colors of the logo as a backdrop to part of the webpage(s)
Should not have
• No "what our clients say" section
• No pictures of people

```html
<!DOCTYPE html>
<html lang="en">
<head>
<meta charset="utf-8">
<title>Harbor Crest Capital</title>
<link href="https://fonts.googleapis.com/css2?family=Montserrat:ital,wght@0,400;0,500;0,600;0,700;1,400&family=Oswald:wght@400&display=swap" rel="stylesheet">
<style>
:root{
  --blue:#1b74c1;
  --blue-dark:#0f5fa8;
  --navy:#10385c;
  --orange:#f5a622;
  --ink:#222;
  --text:#555;
  --muted:#888;
  --panel:#f5f5f5;
  --footer:#2b2a2c;
  --line:#dcdcdc;
}
*{margin:0;padding:0;box-sizing:border-box}
html,body{width:1200px;height:2916px;overflow:hidden}
body{font-family:'Montserrat',sans-serif;color:var(--ink);background:#fff;position:relative}
.abs{position:absolute}
.brand{font-family:'Montserrat',sans-serif;font-weight:600;color:var(--blue);display:flex;align-items:center;gap:10px;font-size:20px;letter-spacing:.5px;line-height:22px}
.brand .mark{width:14px;height:14px;background:var(--blue);flex:none}
.btn{position:absolute;display:flex;align-items:center;justify-content:center;border-radius:20px;font-size:10.5px;font-weight:700;letter-spacing:.6px;text-transform:uppercase}
.btn-solid{background:var(--blue);color:#fff}
.btn-white{background:#fff;color:var(--blue)}
.btn-outline{border:1.5px solid #999;color:var(--blue);background:transparent}

/* header */
.site-header{left:0;top:0;width:1200px;height:84px;background:#fff}
.nav a{position:absolute;top:36px;font-size:10.5px;font-weight:600;color:var(--ink);text-decoration:none;letter-spacing:.4px}
.nav a.active{color:var(--blue)}
.user-btn{left:956px;top:25px;width:34px;height:34px;border:1.5px solid #999;border-radius:50%;display:flex;align-items:center;justify-content:center}

/* hero */
.hero{left:0;top:84px;width:1200px;height:474px;background:linear-gradient(180deg,#6f8397 0%,#9aa2aa 35%,#c88f68 60%,#4c5968 78%,#26313d 100%)}
.hero h1{left:69px;top:158px;font-size:45px;line-height:51px;font-weight:700;color:#fff;letter-spacing:.5px}
.hero-dots{left:1118px;top:207px;display:flex;flex-direction:column;gap:6px}
.hero-dots span{width:11px;height:11px;border:1.5px solid #fff;border-radius:50%}
.hero-dots span.on{background:#fff}

/* about */
.about-photo{left:69px;top:628px;width:475px;height:307px;background:linear-gradient(180deg,#8fa6bb 0%,#b9c3cc 45%,#5d6b78 75%,#3d4854 100%)}
.about-panel{left:474px;top:686px;width:656px;height:321px;background:var(--panel)}
.about h2{left:614px;top:622px;font-size:34px;font-weight:700}
.about p{left:614px;width:450px;font-size:11px;line-height:17px;color:var(--text)}

/* stats */
.stat{top:1060px;width:200px;text-align:center}
.stat .num{font-family:'Oswald',sans-serif;font-size:36px;color:var(--blue);line-height:42px}
.stat .num small{font-size:20px}
.stat .label{font-size:13px;font-style:italic;color:#333;margin-top:2px}
.stat-divider{top:1064px;width:1px;height:70px;background:#bbb}

/* services */
.services{left:0;top:1202px;width:1200px;height:468px;background:linear-gradient(135deg,#2a8cd6 0%,#1b74c1 50%,#0f66b3 100%)}
.eyebrow{left:69px;top:72px;font-size:10.5px;font-weight:700;color:#fff;letter-spacing:.6px;border-left:2px solid #fff;padding-left:12px;line-height:11px}
.services h2{left:69px;top:92px;font-size:36px;font-weight:700;color:#fff}
.service{top:164px;width:230px;color:#fff}
.service .head{display:flex;align-items:center;height:58px}
.service .icon{width:54px;height:56px}
.service .sep{width:1px;height:56px;background:#fff;margin:0 14px 0 12px}
.service h3{font-size:13.5px;font-weight:700;line-height:16px}
.service p{margin-top:22px;font-size:12px;line-height:17px;width:215px}

/* statement */
.statement-text{left:290px;top:1792px;width:620px;text-align:center;font-size:13.5px;line-height:21px;font-style:italic;color:#666}
.statement-dots{left:205px;top:1804px;display:flex;flex-direction:column;gap:6px}
.statement-dots span{width:11px;height:11px;border:1.5px solid var(--blue);border-radius:50%}
.statement-dots span.on{background:var(--blue)}

/* band */
.people-band{left:0;top:1990px;width:1200px;height:140px;background:var(--orange)}
.people-band h2{left:69px;top:57px;font-size:24.5px;font-weight:700;color:#fff;letter-spacing:.3px}

/* contact */
.help h2{left:0;top:2192px;width:1200px;text-align:center;font-size:27px;font-weight:600}
.help p{left:0;top:2235px;width:1200px;text-align:center;font-size:12px;line-height:17px;color:#333}
.field{border:1px solid var(--line);font-size:9.5px;color:#777;padding:10px 13px}

/* footer */
.site-footer{left:0;top:2566px;width:1200px;height:350px;background:var(--footer);color:#bbb}
.site-footer h4{position:absolute;top:68px;font-size:13px;font-weight:700;color:#fff;letter-spacing:.3px}
.site-footer ul{position:absolute;top:104px;list-style:none;font-size:11.5px;line-height:21px;color:#aaa}
.social{display:flex;gap:6px}
.social span{width:22px;height:22px;border:1.5px solid var(--blue);border-radius:50%}
.social span.on{background:var(--blue)}
</style>
</head>
<body>

<header class="abs site-header">
  <div class="abs brand" style="left:69px;top:30px"><span class="mark"></span>HARBOR CREST CAPITAL</div>
  <nav class="nav">
    <a class="active" style="left:477px">HOME</a>
    <a style="left:560px">ABOUT US</a>
    <a style="left:666px">SERVICES</a>
    <a style="left:769px">REVIEWS</a>
    <a style="left:869px">CAREERS</a>
  </nav>
  <div class="abs user-btn"><svg width="12" height="12" viewBox="0 0 12 12"><circle cx="6" cy="4" r="2.3" fill="#1b74c1"/><path d="M1.8 11c0-2.6 1.9-4 4.2-4s4.2 1.4 4.2 4z" fill="#1b74c1"/></svg></div>
  <div class="btn btn-solid" style="left:1004px;top:25px;width:126px;height:34px">Contact Us</div>
</header>

<section class="abs hero" role="img" aria-label="Manhattan skyscraper skyline across the river at sunset">
  <h1 class="abs">MANAGE YOUR<br>PORTFOLIO WITH HCC</h1>
  <div class="btn btn-white" style="left:70px;top:274px;width:126px;height:34px">Get a Quote</div>
  <div class="abs hero-dots"><span></span><span></span><span class="on"></span><span></span></div>
  <svg class="abs" style="left:592px;top:380px" width="16" height="24" viewBox="0 0 16 24"><path d="M8 1v21M2 16l6 6 6-6" stroke="#fff" stroke-width="2" fill="none"/></svg>
</section>

<section class="about">
  <div class="abs about-panel"></div>
  <div class="abs about-photo" role="img" aria-label="Chicago downtown skyscrapers seen from street level"></div>
  <h2 class="abs">ABOUT HCC</h2>
  <p class="abs" style="top:718px">There are many variations of passages of Lorem Ipsum available, but the majority have suffered alteration in some form, by injected humour, or work kdomised words which don't look even slightly believable. If you are going to use a passage of Lorem Ipsum, you need to be sure there isn't anything embarrass-ing hidden in the middle of text.</p>
  <p class="abs" style="top:818px">All the Lorem Ipsum generators on the Internet tend to repeat predefined chunks as necessary, making this the first true generator on the Internet. It uses a dictionary of over 200 Latin words, combined.</p>
  <div class="btn btn-outline" style="left:614px;top:900px;width:126px;height:35px">Contact Us</div>
</section>

<section class="stats">
  <div class="abs stat" style="left:228px"><div class="num">40<small>yrs</small></div><div class="label">Investment Experience</div></div>
  <div class="abs stat-divider" style="left:464px"></div>
  <div class="abs stat" style="left:500px"><div class="num"><small>$</small>68.4<small>B</small></div><div class="label">Assets Under Management</div></div>
  <div class="abs stat-divider" style="left:736px"></div>
  <div class="abs stat" style="left:772px"><div class="num">200<small>+</small></div><div class="label">Contrary to popular</div></div>
</section>

<section class="abs services">
  <div class="abs eyebrow">WHAT WE OFFER</div>
  <h2 class="abs">OUR SERVICES</h2>

  <div class="abs service" style="left:69px">
    <div class="head">
      <svg class="icon" viewBox="0 0 54 56" fill="none" stroke="#fff" stroke-width="2"><ellipse cx="14" cy="30" rx="12" ry="4"/><path d="M2 30v16c0 2 5 4 12 4s12-2 12-4V30M2 38c0 2 5 4 12 4s12-2 12-4"/><circle cx="40" cy="12" r="8" stroke="#f5a622"/><path d="M40 20v34M40 34l-8-6M40 42l8-6" stroke="#f5a622"/></svg>
      <div class="sep"></div><h3>Investment<br>Advisory</h3>
    </div>
    <p>Lorem Ipsum is simply dummy text of the printing and typesetting industry. Lorem Ipsum has been the industry's standard dummy text ever since the 1500s.</p>
  </div>

  <div class="abs service" style="left:342px">
    <div class="head">
      <svg class="icon" viewBox="0 0 54 56" fill="none" stroke="#fff" stroke-width="2"><rect x="14" y="4" width="24" height="16"/><circle cx="7" cy="22" r="4"/><circle cx="47" cy="22" r="4"/><path d="M2 34h50M6 34v20M48 34v20M14 34v20M22 34v20M30 34v20M38 34v20"/></svg>
      <div class="sep"></div><h3>Financial<br>Consulting</h3>
    </div>
    <p>Lorem Ipsum is simply dummy text of the printing and typesetting industry. Lorem Ipsum has been the industry's standard dummy text ever since the 1500s.</p>
  </div>

  <div class="abs service" style="left:614px">
    <div class="head">
      <svg class="icon" viewBox="0 0 54 56" fill="none" stroke="#fff" stroke-width="2"><circle cx="26" cy="10" r="7" stroke="#f5a622"/><path d="M6 36c0-9 9-15 20-15s20 6 20 15-8 14-20 14S6 45 6 36zM14 48v6M36 48v6"/></svg>
      <div class="sep"></div><h3>Financial<br>Planning</h3>
    </div>
    <p>Lorem Ipsum is simply dummy text of the printing and typesetting industry. Lorem Ipsum has been the industry's standard dummy text ever since the 1500s.</p>
  </div>

  <div class="abs service" style="left:886px">
    <div class="head">
      <svg class="icon" viewBox="0 0 54 56" fill="none" stroke="#fff" stroke-width="2"><rect x="3" y="2" width="38" height="52"/><path d="M10 12h20M10 20h24M10 28h16M10 36h12"/><circle cx="40" cy="40" r="10" stroke="#f5a622"/></svg>
      <div class="sep"></div><h3>Portfolio<br>Management</h3>
    </div>
    <p>Lorem Ipsum is simply dummy text of the printing and typesetting industry. Lorem Ipsum has been the industry's standard dummy text ever since the 1500s.</p>
  </div>

  <div class="btn btn-white" style="left:537px;top:359px;width:126px;height:34px">Get a Quote</div>
</section>

<section class="statement">
  <svg class="abs" style="left:578px;top:1738px" width="44" height="32" viewBox="0 0 44 32"><path d="M2 32V16L10 0h8l-6 14h6v18zM26 32V16L34 0h8l-6 14h6v18z" fill="#f5a622"/></svg>
  <div class="abs statement-dots"><span></span><span></span><span class="on"></span><span></span></div>
  <p class="abs statement-text">There are many variations of passages of Lorem Ipsum available, but the majority have suffered alteration in some form, by injected humour, or randomised words which don't look even slightly believable. If you are going to use a passage of Lorem Ipsum, you need to be sure there isn't anything embarrassing hidden.</p>
  <div class="abs" style="left:0;top:1894px;width:1200px;text-align:center;font-size:11.5px;font-weight:600;letter-spacing:.5px">OUR APPROACH</div>
  <div class="abs" style="left:0;top:1912px;width:1200px;text-align:center;font-size:11px;color:var(--muted)">philosophy</div>
</section>

<section class="abs people-band">
  <h2 class="abs">WE KNOW OUR PEOPLE ARE OUR BIGGEST DIFFERENTIATOR.</h2>
  <div class="btn btn-solid" style="left:1004px;top:53px;width:126px;height:34px">Careers</div>
</section>

<section class="help">
  <h2 class="abs">HOW CAN WE HELP YOU TODAY?</h2>
  <p class="abs">Contact us today for a free consultation <span style="color:var(--blue);font-weight:600">555-014-2290</span> or complete the below form. We will respond<br>to your enquiry as soon as possible.</p>
  <div class="abs field" style="left:272px;top:2292px;width:230px;height:30px">Name</div>
  <div class="abs field" style="left:516px;top:2292px;width:230px;height:30px">Email</div>
  <div class="abs field" style="left:760px;top:2292px;width:154px;height:30px">Phone</div>
  <div class="abs field" style="left:272px;top:2335px;width:642px;height:111px">Type your Message ...</div>
  <div class="btn btn-outline" style="left:537px;top:2462px;width:126px;height:34px">Send Message</div>
</section>

<footer class="abs site-footer">
  <div class="abs brand" style="left:69px;top:124px"><span class="mark"></span>HARBOR CREST<br>CAPITAL</div>
  <h4 style="left:342px">CONTACT US</h4>
  <div class="abs" style="left:342px;top:102px;font-size:14px;font-weight:700;color:var(--blue)">Call Us: 555-014-2290</div>
  <div class="abs" style="left:342px;top:122px;font-size:11.5px;color:#bbb">info@harborcrestcapital.com</div>
  <div class="abs" style="left:342px;top:150px;font-size:13px;font-weight:700;color:var(--blue)">HCC</div>
  <div class="abs" style="left:342px;top:170px;font-size:11.5px;line-height:17px;color:#bbb;width:230px">4410 Lakeview Parkway Suite 210, Fairmont, NY 10560</div>

  <h4 style="left:607px">QUICK LINKS</h4>
  <ul style="left:607px"><li>Home</li><li>About Us</li><li>Services</li><li>Reviews</li><li>Careers</li><li>Contact Us</li></ul>

  <h4 style="left:756px">SERVICES</h4>
  <ul style="left:756px"><li>Investment Advisory</li><li>Financial Consulting</li><li>Financial Planning</li><li>Portfolio Management</li></ul>

  <h4 style="left:927px">SUBSCRIBE US</h4>
  <div class="abs" style="left:927px;top:104px;width:203px;height:28px;border-radius:14px;background:#3d3c3f;font-size:10px;color:#ccc;padding:8px 14px">Enter Your Email...</div>
  <svg class="abs" style="left:1106px;top:113px" width="12" height="10" viewBox="0 0 12 10"><path d="M0 0l12 5-12 5 3-5z" fill="#1b74c1"/></svg>
  <div class="abs social" style="left:928px;top:147px"><span class="on"></span><span></span><span></span><span></span></div>

  <div class="abs" style="left:69px;top:265px;width:1061px;height:1px;background:#444"></div>
  <div class="abs" style="left:0;top:301px;width:1200px;text-align:center;font-size:11px;color:#bbb">© 2019 <span style="color:var(--blue)">Harbor Crest Capital.</span> All Right Reserved</div>
  <svg class="abs" style="left:1120px;top:298px" width="16" height="18" viewBox="0 0 16 18"><path d="M8 0l8 18-8-5-8 5z" fill="#1b74c1"/></svg>
</footer>

</body>
</html>
```